Discreet simple classy for adult entertainment

I would like a matte black business card with gold writing for my business. Keeping it simple. Having my following:

Lana frost
Events. Entertainment. Promotions
0491726580

or alternatively could have what i had on my previous card below but i think i prefer the above as again - discretion.

Maybe a nice gold line thru the card or some other very simple design . Or not open to ideas/ can be doublesided if any good ideas with that.

included pics of my old bus card. not sure weather i want a photo on it or not. if i do it wont be the same pic. i kinda wanted a card that was discreet so if it was in someones wallet they wouldn't neccessarily realise it was from a stripper.

Target Market(s)

men

Industry/Entity Type

Business

Contact Information for Business Card

Lana frost
0491726580

Requirements
Nice to have
• i don't know i am really open to anything. im giving my cards to guys so something they can have in their wallet that is discreet preferably.

```html
<!DOCTYPE html>
<html lang="en">
<head>
<meta charset="utf-8">
<title>Lana Frost — Business Card</title>
<link rel="stylesheet" href="https://fonts.googleapis.com/css2?family=Arimo:wght@400;700&display=swap">
<style>
  :root {
    --card-black: #000000;
    --ink-gold: #c9a54e;
  }
  html, body {
    margin: 0;
    padding: 0;
    overflow: hidden;
    background: var(--card-black);
  }
  .business-card {
    position: relative;
    width: 1200px;
    height: 686px;
    background: var(--card-black);
    color: var(--ink-gold);
    font-family: "Arimo", Arial, sans-serif;
    overflow: hidden;
  }
  .card-line {
    position: absolute;
    left: 0;
    width: 100%;
    margin: 0;
    text-align: center;
    line-height: 1;
    white-space: nowrap;
    box-sizing: border-box;
  }
  .card-name {
    top: 196px;
    font-size: 116px;
    font-weight: 700;
    letter-spacing: 15px;
    padding-left: 15px;
  }
  .card-divider {
    position: absolute;
    left: 208px;
    top: 342px;
    width: 784px;
    height: 4px;
    display: block;
  }
  .card-phone {
    top: 381px;
    font-size: 64px;
    font-weight: 700;
    letter-spacing: 16px;
    padding-left: 16px;
  }
  .card-services {
    top: 594px;
    font-size: 50px;
    font-weight: 400;
    letter-spacing: 1.4px;
    padding-left: 1.4px;
  }
</style>
</head>
<body>
  <main class="business-card">
    <h1 class="card-line card-name">LANA FROST</h1>
    <svg class="card-divider" viewBox="0 0 784 4" aria-hidden="true">
      <rect x="0" y="0" width="784" height="4" fill="var(--ink-gold)"/>
    </svg>
    <p class="card-line card-phone">0491726580</p>
    <p class="card-line card-services">EVENTS | ENTERTAINMENT | PROMOTIONS</p>
  </main>
</body>
</html>
```